Fitness ,martial arts and strength and conditioning training

A flyer showing that the lantern sports and fitness offers
-mma,Brazilian jiu Jitsu, Muay Thai kickboxing and self defence also group fitness classes in strength and conditioning,cardio kickboxing ,high intensity interval training and weight training.open to all ages ,youth programs available,open to beginners to advanced.one on one sessions also available.
Daily classes
Bjj :led by bjj tas black belt gavin Presk and Corey Maddox, bjj will help with self confidence,strength and flexibility whilst learning to defend against larger opponents.
Mma :learn to become well rounded in all styles of martial arts from the ground to technical striking and takedowns
Women's Cardio kickboxing:a great way to get fit whilst learning a variety of striking techniques including kicks knees and elbow strikes ,great for all ages and fitness levels.classes consist of pad and bag work as well as conditioning with bodyweight exercises developing self confidence strength and flexibility.
Youth program:kids classes available for all disciplines ,giving children structure, self confidence and skills to defend themselves whilst having fun and learning discipline.
HIIT Training :high intensity interval training classes consist of circuit style training of upper and lower body exercises using free weights, kettle bells and much more giving full body conditioning and gret cardio.
Additional info contact details:Corey Maddox 0462815730
Facebook :Ridgeway MMA Bramford
Address 27D Tarlow cove Bramford
I would love some pictures of people doing bjj kickboxing and fitness thank you

Target Market(s)

All ages

Industry/Entity Type

Fitness

Font styles to use
Serif
Sans Serif

Requirements
Must have
• A flyer showing that the lantern sports and fitness offers
• -mma,Brazilian jiu Jitsu, Muay Thai kickboxing and self defence also group fitness classes in strength and conditioning,cardio kickboxing ,high intensity interval training and weight training.open to all ages ,youth programs available,open to beginners to advanced.one on one sessions also available.
• Daily classes
• Bjj :led by bjj tas black belt gavin Presk and Corey Maddox, bjj will help with self confidence,strength and flexibility whilst learning to defend against larger opponents.
• Mma :learn to become well rounded in all styles of martial arts from the ground to technical striking and takedowns
• Women's Cardio kickboxing:a great way to get fit whilst learning a variety of striking techniques including kicks knees and elbow strikes ,great for all ages and fitness levels.classes consist of pad and bag work as well as conditioning with bodyweight exercises developing self confidence strength and flexibility.
• Youth program:kids classes available for all disciplines ,giving children structure, self confidence and skills to defend themselves whilst having fun and learning discipline.
• HIIT Training :high intensity interval training classes consist of circuit style training of upper and lower body exercises using free weights, kettle bells and much more giving full body conditioning and gret cardio.
• Additional info contact details:Corey Maddox 0462815730
• Facebook :Ridgeway MMA Bramford
• Address 27D Tarlow cove Bramford
• I would love some pictures of people doing bjj kickboxing and fitness thank you
Nice to have
• All the above
Should not have
• Pink colour

```html
<!DOCTYPE html>
<html lang="en">
<head>
<meta charset="utf-8">
<title>The Lantern Sports and Fitness – Flyer</title>
<link href="https://fonts.googleapis.com/css2?family=Roboto:wght@400;700;900&family=Roboto+Condensed:wght@700&display=swap" rel="stylesheet">
<style>
  :root {
    --sky-top: #c9d6e0;
    --sky-mid: #8fa5b8;
    --sky-low: #4f6478;
    --ground: #2a3746;
    --red: #d81e1e;
    --white: #ffffff;
    --badge: #1b1b1b;
    --logo-box: #ffffff;
    --logo-text: #1d1d1d;
  }
  * { margin: 0; padding: 0; box-sizing: border-box; }
  html, body { width: 849px; height: 1200px; overflow: hidden; }
  body { font-family: "Roboto", Arial, sans-serif; background: var(--ground); }
  .flyer { position: relative; width: 849px; height: 1200px; overflow: hidden; }
  .backdrop {
    position: absolute; inset: 0;
    background:
      radial-gradient(ellipse 260px 420px at 640px 540px, rgba(240,240,240,0.55), rgba(240,240,240,0) 70%),
      linear-gradient(180deg, var(--sky-top) 0%, var(--sky-mid) 38%, var(--sky-low) 70%, var(--ground) 100%);
  }
  .headline {
    position: absolute; top: 30px; left: 0; width: 100%;
    text-align: center; color: var(--red);
    font-family: "Roboto Condensed", Arial, sans-serif; font-weight: 700;
    font-size: 30px; letter-spacing: 1px; text-transform: uppercase;
  }
  .classes { position: absolute; left: 113px; top: 92px; width: 430px; }
  .class { margin-bottom: 26px; }
  .class h2 {
    color: var(--white); font-weight: 900; font-size: 27px;
    text-transform: uppercase; line-height: 1.1; margin-bottom: 6px;
  }
  .class p { color: var(--red); font-size: 14px; line-height: 1.38; font-weight: 700; }
  .club-badge { position: absolute; left: 595px; top: 580px; }
  .join {
    position: absolute; left: 620px; top: 815px;
    color: var(--red); font-weight: 900; font-size: 36px; text-transform: uppercase;
  }
  .brand-box {
    position: absolute; left: 156px; top: 976px; width: 156px; height: 156px;
    background: var(--logo-box);
    display: flex; align-items: center; justify-content: center; text-align: center;
  }
  .brand-box span { color: var(--logo-text); font-weight: 900; font-size: 24px; line-height: 1.05; text-transform: uppercase; }
  .contact { position: absolute; left: 338px; top: 985px; color: var(--white); }
  .contact .name { color: var(--red); font-weight: 900; font-size: 38px; margin-bottom: 6px; }
  .contact .row { display: flex; align-items: center; gap: 12px; font-size: 22px; font-weight: 700; margin-bottom: 6px; }
  .contact .row.small { font-size: 19px; }
  .contact svg { flex: none; }
</style>
</head>
<body>
<main class="flyer">
  <div class="backdrop" role="img" aria-label="Photo of a woman in a white martial arts uniform performing a high kick against a cloudy blue sky"></div>

  <h1 class="headline">Gym - Martial Arts - Fitness Center</h1>

  <section class="classes">
    <article class="class">
      <h2>BJJ</h2>
      <p>Led by bjj tas black belt gavin Presk and Corey Maddox, bjj will help with self confidence,strength and flexibility whilst learning to defend against larger opponents.</p>
    </article>
    <article class="class">
      <h2>MMA</h2>
      <p>Learn to become well rounded in all styles of martial arts from the ground to technical striking and takedowns</p>
    </article>
    <article class="class">
      <h2>Women's Cardio Kickboxing</h2>
      <p>A great way to get fit whilst learning a variety of striking techniques including kicks,knees and elbow strikes ,great for all ages and fitness levels.classes consist of pad and bag work as well as conditioning with bodyweight exercises developing self confidence strength and flexibility.</p>
    </article>
    <article class="class">
      <h2>Youth Program</h2>
      <p>Kids classes available for all disciplines ,giving children structure, self confidence and skills to defend themselves whilst having fun and learning discipline.</p>
    </article>
    <article class="class">
      <h2>HIIT Training</h2>
      <p>High intensity interval training classes consist of circuit style training of upper and lower body exercises using free weights, kettle bells and much more giving full body conditioning and great cardio.</p>
    </article>
  </section>

  <svg class="club-badge" width="254" height="254" viewBox="0 0 254 254" aria-hidden="true">
    <circle cx="127" cy="127" r="124" fill="var(--badge)"/>
    <circle cx="127" cy="127" r="100" fill="none" stroke="var(--white)" stroke-width="4"/>
  </svg>

  <div class="join">Join Now!</div>

  <div class="brand-box"><span>The<br>Lantern</span></div>

  <div class="contact">
    <div class="name">Corey Maddox</div>
    <div class="row">
      <svg width="24" height="24" viewBox="0 0 24 24"><circle cx="12" cy="12" r="11" fill="none" stroke="#fff" stroke-width="2"/><path d="M8 6c1-1 2 0 2.5 1.5l.5 1.5-1.2 1.2c.8 1.6 1.9 2.7 3.5 3.5L14.5 12.5l1.5.5c1.5.5 2.5 1.5 1.5 2.5-1 1.2-2.5 1.5-4.5.5-2.5-1.2-4.5-3.2-5.6-5.6C6.5 8.5 7 7 8 6z" fill="#fff"/></svg>
      0462815730
    </div>
    <div class="row small">
      <svg width="18" height="24" viewBox="0 0 18 24"><path d="M9 1C4.6 1 1 4.5 1 9c0 6 8 14 8 14s8-8 8-14c0-4.5-3.6-8-8-8z" fill="#fff"/><circle cx="9" cy="9" r="3" fill="var(--ground)"/></svg>
      27D Tarlow cove Bramford
    </div>
    <div class="row small">
      <svg width="18" height="18" viewBox="0 0 18 18"><circle cx="9" cy="9" r="8" fill="#fff"/></svg>
      Ridgeway MMA Bramford
    </div>
  </div>
</main>
</body>
</html>
```